The Birchfall Reel----- Wade Pellinger----- Umpqua River Smallmouth ------www.thebirchfallreel-demo.com-----

Hello Fishermen,
The Umpqua rivers peaceful beauty is like no other river, the private Loop section offers trophy bass fishing along with 100 fish days. Spin cast or fly fish for bass. This 8 hour fishing trip takes you into a remote section of ranches and wilderness abundant with not only thousands of bass per mile...... but wildlife and scenery are breath taking in this quite section of river.
This trip is for everyone, easy for the Grand Parents and the grand kids...... Women love this trip with the warm weather and easy fishing.
So Let's go Fishing...... please call or email us today and book your trip or with any questions you have.
Vacation Rentals, Motels and R.V parks all available close by.

Email us at: birchfallreel@mailvale-demo.net
Visit our website at: www.thebirchfallreel-demo.com
Call us at: 541-555-0148

Thank you for fishing with us,
Wade Pellinger

return address;
Wade Pellinger
p.o. box 712
Elkton, Oregon 97781

****NOTE for front of post card layout person should go to our website home page for ideas, and photos. Please feel free to change our message above to correct grammar and make read smoother, Thank you.....

there is no contest....not sure how that got there...

```html
<!DOCTYPE html>
<html lang="en">
<head>
<meta charset="utf-8">
<title>The Birchfall Reel – Umpqua River Smallmouth Postcard</title>
<link rel="stylesheet" href="https://fonts.googleapis.com/css2?family=Source+Sans+3:wght@400;600;700&display=swap">
<style>
  :root {
    --river-blue: #0d5f82;
    --sand: #ddd7d0;
    --paper: #ffffff;
    --ink: #1f1f1f;
    --backdrop: #ece9e4;
    --line-grey: #b9b9b9;
    --photo-a: #8c9a86;
    --photo-b: #c9b49a;
    --photo-c: #5f8a6a;
    --photo-d: #2f4f62;
  }
  * { box-sizing: border-box; margin: 0; padding: 0; }
  html, body { width: 1200px; height: 1013px; overflow: hidden; }
  body {
    background: var(--backdrop);
    font-family: "Source Sans 3", sans-serif;
    color: var(--ink);
    position: relative;
  }
  .postcard {
    position: absolute;
    width: 640px;
    height: 440px;
    overflow: hidden;
    box-shadow: 0 6px 18px rgba(0,0,0,0.18);
  }
  .postcard svg.card-art { position: absolute; inset: 0; width: 100%; height: 100%; }

  /* Message side */
  .message-side { left: 40px; top: 40px; background: var(--sand); }
  .message-copy {
    position: absolute; left: 30px; top: 40px; font-size: 13px; line-height: 17px;
  }
  .message-copy p { margin-bottom: 6px; }
  .message-copy .wide { width: 480px; }
  .message-copy .narrow { width: 290px; }
  .message-copy .narrower { width: 230px; }
  .contact-block {
    position: absolute; color: var(--paper); font-size: 14px; line-height: 17px;
  }
  .contact-block p + p { margin-top: 4px; }
  .message-side .contact-block { left: 26px; top: 297px; }
  .sign-off { position: absolute; left: 26px; top: 380px; font-size: 14px; }
  .signature {
    position: absolute; left: 30px; top: 409px; color: var(--paper);
    font-weight: 700; font-size: 19px; letter-spacing: 0.5px; text-transform: uppercase;
  }

  /* Address side */
  .address-side { left: 520px; top: 533px; background: var(--paper); }
  .address-side .contact-block { left: 30px; top: 347px; font-size: 15px; line-height: 18px; }
  .return-address {
    position: absolute; left: 452px; top: 345px; font-size: 12px; line-height: 15px; font-style: normal;
  }
</style>
</head>
<body>

<section class="postcard message-side" aria-label="Postcard message side">
  <svg class="card-art" viewBox="0 0 640 440">
    <defs>
      <linearGradient id="boatPhoto" x1="0" y1="0" x2="1" y2="1">
        <stop offset="0" stop-color="var(--photo-a)"/>
        <stop offset="0.55" stop-color="var(--photo-b)"/>
        <stop offset="1" stop-color="#d8d6d2"/>
      </linearGradient>
    </defs>
    <path d="M603 0 C598 85 530 140 450 190 C350 250 292 325 297 440 L640 440 L640 0 Z" fill="var(--river-blue)"/>
    <path d="M618 0 C612 88 545 146 466 196 C366 257 307 330 311 440" fill="none" stroke="var(--paper)" stroke-width="4"/>
    <rect x="0" y="290" width="320" height="82" fill="var(--river-blue)"/>
    <rect x="0" y="402" width="310" height="38" fill="var(--river-blue)"/>
    <path role="img" aria-label="Photo of the guide holding two river fish on a boat"
          d="M640 0 L640 440 L325 440 C320 330 380 260 480 205 C560 158 628 100 632 0 Z" fill="url(#boatPhoto)"/>
  </svg>

  <div class="message-copy">
    <p>Hello Fishermen,</p>
    <p class="wide">The Umpqua rivers peaceful beauty is like no other river, the private Loop section offers trophy bass fishing along with 100 fish days. Spin cast or fly fish for bass. This 8 hour fishing trip takes you into a remote section of ranches and wilderness abundant with not only thousands of bass per mile...... but wildlife and scenery are breath taking in this quite section of river.</p>
    <p class="narrow">This trip is for everyone, easy for the Grand Parents and the grand kids...... Women love this trip with the warm weather and easy fishing.</p>
    <p class="narrow">So Let's go Fishing...... please call or email us today and book your trip or with any questions you have.</p>
    <p class="narrower">Vacation Rentals, Motels and R.V parks all available close by.</p>
  </div>

  <div class="contact-block">
    <p>Email us at: birchfallreel@mailvale-demo.net</p>
    <p>Visit our website at:<br>www.thebirchfallreel-demo.com</p>
    <p>Call us at: 541-555-0148</p>
  </div>
  <p class="sign-off">Thank you for fishing with us,</p>
  <p class="signature">Wade Pellinger</p>
</section>

<section class="postcard address-side" aria-label="Postcard address side">
  <svg class="card-art" viewBox="0 0 640 440">
    <defs>
      <linearGradient id="riverPhoto" x1="0" y1="0" x2="1" y2="1">
        <stop offset="0" stop-color="var(--photo-c)"/>
        <stop offset="0.6" stop-color="var(--photo-d)"/>
        <stop offset="1" stop-color="#c7cdd2"/>
      </linearGradient>
    </defs>
    <path d="M0 230 L330 230 C400 260 430 360 405 440 L0 440 Z" fill="var(--river-blue)"/>
    <circle cx="165" cy="140" r="202" fill="var(--paper)"/>
    <circle cx="165" cy="140" r="205" fill="none" stroke="var(--line-grey)" stroke-width="1"/>
    <circle role="img" aria-label="Photo of the guide holding a large river fish"
            cx="165" cy="140" r="194" fill="url(#riverPhoto)"/>
    <rect x="560" y="22" width="58" height="70" fill="none" stroke="var(--ink)" stroke-width="1"/>
    <g stroke="var(--line-grey)" stroke-width="1" stroke-dasharray="3 2">
      <line x1="420" y1="175" x2="620" y2="175"/>
      <line x1="420" y1="210" x2="620" y2="210"/>
      <line x1="420" y1="245" x2="620" y2="245"/>
    </g>
  </svg>

  <div class="contact-block">
    <p>Email us at: birchfallreel@mailvale-demo.net</p>
    <p>Visit our website at:<br>www.thebirchfallreel-demo.com</p>
    <p>Call us at: 541-555-0148</p>
  </div>
  <address class="return-address">
    return address;<br>Wade Pellinger<br>p.o. box 712<br>Elkton, Oregon 97781
  </address>
</section>

</body>
</html>
```